Hypothetical Customer Lifecycle

Need a poster to show the lifecycle of a student going through university.

There are three main stages of the lifecycle, it also needs to visually loop back in some way to the start from the end of the 3rd stage.

1) Prospect – Strategy is to Acquire
There are three main sub experiences within this stage which are
a. Decide
b. Apply
c. On board
Within the Prospect stage we also need to show some Needs and Pain Points as below
Needs
• Validation on choices from peers or family
• Clear direction on choices
Pain Points
• Not sure where to start
• Poor navigation and information architecture

2) Current – Strategy is to Engage
a. Commence
b. Study
c. Complete
Within the Current stage we also need to show some Needs and Pain Points as below
Needs
• Access to peer groups and faculty
• Flexibility in modes of learning
Pain Points
• Quality of faculty engagement can vary
• Online tools are hard to use

3) Alumni – Strategy is to Retain
a. Graduate
b. Job Seek
c. Network
Needs
• Options to further career
• Competency based learning
Pain Points
• Lots of irrelevant emails and mail
• Struggle to relate to Alumni programs

Target Market(s)

Exec level, technology managers

Industry/Entity Type

Education

Font styles to use
Sans Serif

Colors
1696d0
ecf7fb
3176b5
ffffff

Requirements
Must have
• Simple visual elements
Should not have
• Try and avoid arrows, chevrons anything that strongly implies a process.

```html
<!DOCTYPE html>
<html lang="en">
<head>
<meta charset="utf-8">
<title>Hypothetical Customer Lifecycle</title>
<link rel="stylesheet" href="https://fonts.googleapis.com/css2?family=Oswald:wght@500;700&family=Arimo:ital,wght@0,400;0,700;1,700&display=swap">
<style>
  :root {
    --navy: #2b1f78;
    --cyan: #1696d0;
    --sky: #c8e6f8;
    --sky-light: #ddf0fb;
    --mist: #ecf7fb;
    --white: #ffffff;
    --loop: #d8322a;
    --stage: #dcdcdc;
  }
  html, body {
    margin: 0;
    width: 1200px;
    height: 1200px;
    overflow: hidden;
    background: var(--stage);
  }
  .poster {
    position: absolute;
    left: 10px;
    top: 182px;
    width: 1181px;
    height: 832px;
  }
  .title { font-family: "Oswald", sans-serif; font-weight: 700; fill: var(--white); }
  .step { font-family: "Oswald", sans-serif; font-weight: 500; fill: var(--white); font-size: 24px; }
  .stage-word { font-family: "Arimo", sans-serif; font-weight: 700; fill: var(--white); }
  .role-label { font-family: "Arimo", sans-serif; font-weight: 700; fill: var(--navy); }
  .heading { font-family: "Arimo", sans-serif; font-weight: 700; fill: var(--navy); font-size: 26px; }
  .point { font-family: "Arimo", sans-serif; fill: var(--cyan); font-size: 18px; }
  .point.strong { font-weight: 700; }
  .node-label { font-family: "Arimo", sans-serif; font-weight: 700; fill: var(--navy); }
  .bar { fill: var(--navy); }
  .loop { fill: none; stroke: var(--loop); stroke-width: 2.5; stroke-dasharray: 3 4; }
</style>
</head>
<body>
<svg class="poster" viewBox="12 228 1476 1040" xmlns="http://www.w3.org/2000/svg">
  <!-- backgrounds -->
  <rect x="12" y="228" width="1476" height="1040" fill="var(--white)"/>
  <rect x="12" y="228" width="1476" height="615" fill="var(--mist)" opacity="0.6"/>
  <polygon points="12,843 565,843 565,815 995,815 995,843 1488,843 1488,1268 12,1268" fill="var(--sky)"/>
  <polygon points="280,1268 552,995 1000,995 1100,1268" fill="var(--white)"/>
  <polygon points="300,1268 565,1003 995,1003 1088,1268" fill="var(--sky-light)"/>

  <!-- title banner -->
  <path class="bar" d="M318,228 H1095 Q1122,240 1120,300 L1095,325 L1080,305 L1060,330 L1040,312 L1020,333 L1000,312 L980,333 L960,312 L940,333 L920,312 L900,333 L880,312 L860,333 L840,312 L820,333 L800,312 L780,333 L760,312 L740,333 L720,312 L700,333 L680,312 L660,333 L640,312 L620,333 L600,312 L580,333 L560,312 L540,333 L520,312 L500,333 L480,312 L460,333 L440,312 L420,333 L400,312 L380,333 L360,312 L340,333 L320,312 L302,333 V250 Q302,228 318,228 Z"/>
  <text class="title" x="704" y="293" font-size="52" text-anchor="middle" textLength="765" lengthAdjust="spacingAndGlyphs">HYPATHETICAL CUSTOMER LIFESTYLE</text>

  <!-- loop path -->
  <path class="loop" d="M132,598 Q95,700 120,815 H1305 L1272,585"/>
  <path class="loop" d="M372,570 L418,593 L1178,470"/>

  <!-- prospect portrait -->
  <circle cx="243" cy="483" r="160" fill="#d4ebf9"/>
  <circle cx="243" cy="483" r="137" fill="#8d949c" role="img" aria-label="Photo of a prospective student reading"/>
  <text class="role-label" x="253" y="583" font-size="30" text-anchor="middle">PROSPECT</text>

  <!-- alumni illustration -->
  <rect x="1165" y="310" width="205" height="250" rx="18" fill="#c9b6a4" role="img" aria-label="Illustration of two alumni reading a book together"/>
  <text class="role-label" x="1155" y="378" font-size="22" font-style="italic">ALUMNI</text>

  <!-- poles with arrowheads -->
  <g class="bar">
    <rect x="142" y="760" width="6" height="40"/><polygon points="135,795 155,795 145,815"/>
    <rect x="279" y="730" width="6" height="70"/><rect x="276" y="726" width="12" height="12"/><polygon points="272,795 292,795 282,815"/>
    <rect x="414" y="708" width="6" height="92"/><rect x="411" y="704" width="12" height="12"/><polygon points="407,795 427,795 417,815"/>
    <rect x="549" y="680" width="6" height="120"/><polygon points="542,795 562,795 552,815"/>
    <rect x="684" y="680" width="6" height="120"/><polygon points="677,795 697,795 687,815"/>
    <rect x="819" y="640" width="6" height="160"/><rect x="816" y="637" width="12" height="12"/><polygon points="812,795 832,795 822,815"/>
    <rect x="954" y="620" width="6" height="180"/><rect x="951" y="617" width="12" height="12"/><polygon points="947,795 967,795 957,815"/>
    <rect x="1089" y="640" width="6" height="160"/><polygon points="1082,795 1102,795 1092,815"/>
    <rect x="1224" y="640" width="6" height="160"/><polygon points="1217,795 1237,795 1227,815"/>
    <rect x="1359" y="576" width="6" height="224"/><rect x="1356" y="573" width="12" height="12"/><polygon points="1352,795 1372,795 1362,815"/>
  </g>

  <!-- step flags -->
  <g>
    <polygon class="bar" points="145,758 280,750 280,785 145,790"/>
    <text class="step" x="206" y="781" text-anchor="middle" transform="rotate(-3 206 775)">DECIDE</text>
    <polygon class="bar" points="282,758 415,748 415,783 282,790"/>
    <text class="step" x="348" y="780" text-anchor="middle" transform="rotate(-3 348 772)">APPLY</text>
    <polygon class="bar" points="417,755 550,746 550,780 417,790"/>
    <text class="step" x="484" y="779" text-anchor="middle" transform="rotate(-3 484 770)">ONBOARD</text>

    <polygon class="bar" points="552,670 685,660 685,695 552,705"/>
    <text class="step" x="618" y="692" text-anchor="middle" transform="rotate(-3 618 684)">COMMENCE</text>
    <polygon class="bar" points="687,665 820,660 820,697 687,705"/>
    <text class="step" x="752" y="693" text-anchor="middle" transform="rotate(-2 752 685)">STUDY</text>
    <polygon class="bar" points="822,668 955,660 955,697 822,705"/>
    <text class="step" x="888" y="692" text-anchor="middle" transform="rotate(-2 888 684)">COMPLETE</text>

    <polygon class="bar" points="960,730 1092,718 1092,752 960,762"/>
    <text class="step" x="1024" y="750" text-anchor="middle" transform="rotate(-4 1024 742)">GRADUATE</text>
    <polygon class="bar" points="1094,727 1225,716 1225,750 1094,760"/>
    <text class="step" x="1158" y="748" text-anchor="middle" transform="rotate(-4 1158 740)">JOB SEEK</text>
    <polygon class="bar" points="1229,728 1358,716 1358,750 1229,760"/>
    <text class="step" x="1293" y="748" text-anchor="middle" transform="rotate(-4 1293 740)">NETWORK</text>
  </g>

  <!-- strategy words -->
  <g transform="rotate(-7 225 715)">
    <polygon class="bar" points="118,693 318,693 338,715 318,737 118,737"/>
    <text class="stage-word" x="218" y="728" font-size="34" text-anchor="middle">STRATEGY</text>
  </g>
  <polygon class="bar" points="346,656 532,650 550,672 532,695 346,700"/>
  <text class="stage-word" x="437" y="688" font-size="34" text-anchor="middle" transform="rotate(-1 437 676)">ACQUIRE</text>
  <g transform="rotate(-10 745 580)">
    <polygon class="bar" points="610,548 850,548 882,580 850,612 610,612"/>
    <text class="stage-word" x="730" y="597" font-size="46" text-anchor="middle">ENGAGE</text>
  </g>
  <polygon class="bar" points="980,563 1290,563 1335,605 1290,648 980,648"/>
  <text class="stage-word" x="1137" y="628" font-size="60" text-anchor="middle">RETAIN</text>

  <!-- prospect needs -->
  <g>
    <rect x="88" y="858" width="19" height="19" fill="none" stroke="var(--navy)" stroke-width="2.5"/>
    <text class="heading" x="123" y="877">Needs</text>
    <text class="point strong" x="84" y="906">• Validation on choices from peers or family</text>
    <text class="point strong" x="84" y="928">• Clear direction on choices</text>
    <rect x="88" y="941" width="19" height="19" fill="none" stroke="var(--navy)" stroke-width="2.5"/>
    <text class="heading" x="123" y="961">Pain Points</text>
    <text class="point" x="84" y="986">• Not sure where to start</text>
    <text class="point" x="84" y="1007">• Poor navigation and information architecture</text>
  </g>

  <!-- current needs -->
  <g>
    <rect x="611" y="831" width="19" height="19" fill="none" stroke="var(--navy)" stroke-width="2.5"/>
    <text class="heading" x="646" y="850">Needs</text>
    <text class="point strong" x="602" y="876">• Access to peer groups and faculty</text>
    <text class="point strong" x="602" y="897">• Flexibility in modes of learning</text>
    <rect x="611" y="914" width="19" height="19" fill="none" stroke="var(--navy)" stroke-width="2.5"/>
    <text class="heading" x="646" y="934">Pain Points</text>
    <text class="point strong" x="598" y="960">• Quality of faculty engagement can vary</text>
    <text class="point strong" x="598" y="981">• Online tools are hard to use</text>
  </g>

  <!-- alumni needs -->
  <g>
    <rect x="1066" y="887" width="19" height="19" fill="none" stroke="var(--navy)" stroke-width="2.5"/>
    <text class="heading" x="1101" y="906">Needs</text>
    <text class="point strong" x="1052" y="932">• Options to further career</text>
    <text class="point strong" x="1052" y="953">• Competency based learning</text>
    <rect x="1066" y="969" width="19" height="19" fill="none" stroke="var(--navy)" stroke-width="2.5"/>
    <text class="heading" x="1101" y="990">Pain Points</text>
    <text class="point" x="1056" y="1015">• Lots of irrelevant emails and mail</text>
    <text class="point" x="1056" y="1037">• Struggle to relate to Alumni programs</text>
  </g>

  <!-- sentient analysis -->
  <text class="node-label" x="420" y="1175" font-size="24" font-style="italic" transform="rotate(-45 420 1175)">Sentient Analysis</text>
  <g stroke="var(--navy)" stroke-width="3" fill="none">
    <line x1="535" y1="1170" x2="680" y2="1090"/>
    <line x1="680" y1="1090" x2="785" y2="1170"/>
    <line x1="785" y1="1170" x2="890" y2="1110"/>
  </g>
  <!-- current: stacked books -->
  <g class="bar">
    <rect x="638" y="1047" width="80" height="18" rx="3"/>
    <rect x="644" y="1070" width="76" height="18" rx="3"/>
    <rect x="640" y="1093" width="82" height="18" rx="3"/>
    <rect x="646" y="1116" width="70" height="14" rx="3"/>
  </g>
  <text class="node-label" x="679" y="1037" font-size="22" text-anchor="middle">Current</text>
  <!-- on campus -->
  <g class="bar">
    <rect x="505" y="1160" width="58" height="34"/>
    <polygon points="505,1160 520,1143 535,1160"/>
    <polygon points="533,1160 548,1143 563,1160"/>
  </g>
  <text class="node-label" x="532" y="1230" font-size="28" text-anchor="middle">On Campus</text>
  <!-- international -->
  <circle cx="787" cy="1175" r="42" fill="var(--navy)" stroke="var(--white)" stroke-width="3"/>
  <text class="node-label" x="788" y="1238" font-size="22" text-anchor="middle">International</text>
  <!-- distance learning: computers -->
  <g class="bar">
    <rect x="910" y="1023" width="34" height="26"/><rect x="914" y="1052" width="26" height="6"/>
    <rect x="873" y="1076" width="34" height="26"/><rect x="877" y="1105" width="26" height="6"/>
    <rect x="947" y="1076" width="34" height="26"/><rect x="951" y="1105" width="26" height="6"/>
  </g>
  <g stroke="var(--navy)" stroke-width="2">
    <line x1="915" y1="1065" x2="905" y2="1078"/>
    <line x1="937" y1="1065" x2="947" y2="1078"/>
    <line x1="912" y1="1090" x2="942" y2="1090"/>
  </g>
  <text class="node-label" x="920" y="1136" font-size="21" text-anchor="middle">Distance Learning</text>
</svg>
</body>
</html>
```